PROMOTION CARD for NEW APPLICATION LAUNCH

Hi need double sided promotion card the size of a postcard.
we car launching a new app, and need to promote
the app is focused on the automotive
the functions are to help remind customers when there car utilities bills are due.
* registration
*Insurance
*CTP due
*Service
* Warranty

Helps sell your car under the ( "Whats New " Button )
Helps you find a better finance or insurance deal.( Zentra Buddy)

Target Market(s)

All consumers who own a Car all ages both male and female

Industry/Entity Type

Automotive

Font styles to use
Sans Serif

Colors
0293ce
9ccb3b
fffbf0

Requirements
Must have
• clean and professional makes you want to down load the app
Nice to have
• clear description about what the app dose feature and functions
• the application will reminder the customer when the
• *registration due
• * insurance due
• *Finance due
• Kavira picture
• car or road in background
• *CTP due
• *Service due
• *Warranty Due
• it will also pay a payment function so you can pay,
Should not have
• color brown/ no running writing

```html
<!DOCTYPE html>
<html lang="en">
<head>
<meta charset="utf-8">
<title>Drivio – App for Automotive Solution</title>
<link href="https://fonts.googleapis.com/css2?family=Fira+Sans:wght@400;600;700&display=swap" rel="stylesheet">
<style>
:root{
  --blue:#1a8fd2;
  --blue-deep:#0f7cc0;
  --green:#9ccb3b;
  --green-dark:#6fa31f;
  --white:#ffffff;
  --ink:#222222;
  --red:#e02424;
  --phone-rim:#e8c2b4;
  --screen-bar:#555a5e;
}
*{box-sizing:border-box;margin:0;padding:0}
html,body{width:1200px;height:889px;overflow:hidden;background:var(--white)}
body{font-family:"Fira Sans",Arial,sans-serif;position:relative}
.card{position:absolute;inset:0;overflow:hidden;background:var(--white)}
.top-band{position:absolute;left:0;top:0;width:1200px;height:170px;background:var(--blue)}
.bottom-wave{position:absolute;left:0;top:0}
.logo-tile{position:absolute;left:46px;top:45px;width:186px;height:210px;background:var(--white);border-radius:16px;display:flex;flex-direction:column;align-items:center;justify-content:center;gap:18px}
.logo-mark{width:96px;height:96px;background:var(--blue);border-radius:6px}
.logo-name{font-size:42px;font-weight:600;color:var(--ink);letter-spacing:1px}
.headline{position:absolute;left:639px;top:66px;font-size:36px;font-weight:600;color:var(--white)}
.intro{position:absolute;left:639px;top:180px;width:520px;font-size:27px;font-weight:600;color:var(--blue);line-height:39px}
.reminders{position:absolute;left:641px;top:275px;list-style:none}
.reminders li{display:flex;align-items:center;gap:10px;height:52px;font-size:31px;font-weight:600;color:var(--blue)}
.reminders svg{width:22px;height:22px;flex:none}
.phone{position:absolute;left:257px;top:58px;width:333px;height:764px;border-radius:52px;background:#f6f6f6;border:5px solid var(--phone-rim);box-shadow:0 4px 10px rgba(0,0,0,.25)}
.phone-camera{position:absolute;left:111px;top:42px;width:12px;height:12px;border-radius:50%;background:#2b3440}
.phone-speaker{position:absolute;left:140px;top:44px;width:56px;height:6px;border-radius:3px;background:#3a3a3a}
.phone-sensor{position:absolute;left:163px;top:20px;width:8px;height:8px;border-radius:50%;background:#222}
.screen{position:absolute;left:12px;top:84px;width:298px;height:606px;background:var(--white);overflow:hidden}
.status-bar{height:20px;background:var(--screen-bar);color:var(--white);font-size:10px;display:flex;justify-content:space-between;align-items:center;padding:0 6px}
.nav-bar{height:30px;background:var(--screen-bar);color:var(--white);display:flex;align-items:center;justify-content:center;font-size:18px;position:relative}
.nav-bar .menu{position:absolute;left:10px;top:9px;width:12px;height:10px;border-top:1.5px solid #ddd;border-bottom:1.5px solid #ddd}
.nav-bar .menu::after{content:"";position:absolute;left:0;top:3px;width:12px;border-top:1.5px solid #ddd}
.hero-photo{position:absolute;left:0;top:55px;width:298px;height:495px;background:linear-gradient(180deg,#7f97ad 0%,#b9c4cc 30%,#3d5fb5 55%,#1c2e7a 80%,#3b3f48 100%)}
.feature-grid{position:absolute;left:0;top:60px;width:298px;display:grid;grid-template-columns:repeat(3,1fr);row-gap:10px}
.feature{display:flex;flex-direction:column;align-items:center;position:relative;height:100px}
.feature-icon{width:58px;height:58px;border-radius:50%;background:#e6e6e6;border:4px solid var(--green);box-shadow:0 2px 3px rgba(0,0,0,.4)}
.feature-label{margin-top:6px;font-size:10px;color:var(--white);text-align:center;line-height:11px;text-shadow:0 1px 2px #000}
.badge{position:absolute;top:-4px;left:58px;width:15px;height:15px;border-radius:50%;background:var(--red);color:var(--white);font-size:9px;display:flex;align-items:center;justify-content:center}
.pill{position:absolute;left:48px;width:210px;height:38px;border-radius:19px;color:var(--white);font-size:15px;display:flex;align-items:center;justify-content:center;border:2px solid #e9f4fb}
.pill-helper{top:458px;background:linear-gradient(180deg,#6cc6f2,#0d7fc4)}
.pill-new{top:514px;background:linear-gradient(180deg,#b6e27a,#55a515)}
.toolbar{position:absolute;left:0;top:556px;width:298px;height:50px;display:flex;justify-content:space-between;align-items:center;padding:0 10px;border-top:1px solid #ddd}
.toolbar svg{width:22px;height:22px}
.callout{position:absolute;background:var(--blue);color:var(--white);font-weight:600;border-radius:6px;box-shadow:3px 4px 4px rgba(0,0,0,.3);text-align:center}
.callout-deal{left:572px;top:576px;width:368px;height:90px;font-size:27px;line-height:33px;padding-top:11px}
.callout-sell{left:330px;top:744px;width:298px;height:65px;font-size:27px;line-height:65px}
.pay-note{position:absolute;left:665px;top:740px;font-size:27px;font-weight:600;color:var(--white);line-height:33px}
</style>
</head>
<body>
<div class="card">
  <div class="top-band"></div>
  <svg class="bottom-wave" width="1200" height="889" viewBox="0 0 1200 889">
    <path d="M0 734 C300 600 650 530 900 540 C1050 546 1150 570 1200 586 L1200 889 L0 889 Z" fill="var(--green)"/>
  </svg>

  <div class="logo-tile">
    <div class="logo-mark"></div>
    <div class="logo-name">Drivio</div>
  </div>

  <h1 class="headline">App for Automotive Solution</h1>
  <p class="intro">The functions are to help remind you when your car utilities bills are due.</p>
  <ul class="reminders">
    <li><svg viewBox="0 0 22 22"><circle cx="11" cy="11" r="9" fill="none" stroke="var(--red)" stroke-width="3"/><path d="M6.5 11 L10 14.5 L16 8" fill="none" stroke="var(--red)" stroke-width="3"/></svg>Registration</li>
    <li><svg viewBox="0 0 22 22"><circle cx="11" cy="11" r="9" fill="none" stroke="var(--red)" stroke-width="3"/><path d="M6.5 11 L10 14.5 L16 8" fill="none" stroke="var(--red)" stroke-width="3"/></svg>Insurance</li>
    <li><svg viewBox="0 0 22 22"><circle cx="11" cy="11" r="9" fill="none" stroke="var(--red)" stroke-width="3"/><path d="M6.5 11 L10 14.5 L16 8" fill="none" stroke="var(--red)" stroke-width="3"/></svg>CTP due</li>
    <li><svg viewBox="0 0 22 22"><circle cx="11" cy="11" r="9" fill="none" stroke="var(--red)" stroke-width="3"/><path d="M6.5 11 L10 14.5 L16 8" fill="none" stroke="var(--red)" stroke-width="3"/></svg>Service</li>
    <li><svg viewBox="0 0 22 22"><circle cx="11" cy="11" r="9" fill="none" stroke="var(--red)" stroke-width="3"/><path d="M6.5 11 L10 14.5 L16 8" fill="none" stroke="var(--red)" stroke-width="3"/></svg>Warranty</li>
  </ul>

  <div class="phone">
    <div class="phone-sensor"></div>
    <div class="phone-camera"></div>
    <div class="phone-speaker"></div>
    <div class="screen">
      <div class="status-bar"><span>●●●●● Norvia 4G</span><span>10:03 am</span><span>▮▮▮</span></div>
      <div class="nav-bar"><span class="menu"></span>Drivio</div>
      <div class="hero-photo" role="img" aria-label="Photo of a blue sports car on a coastal road with palm trees"></div>
      <div class="feature-grid">
        <div class="feature"><div class="feature-icon"></div><div class="feature-label">Contract &amp;<br>Receipt Box</div></div>
        <div class="feature"><span class="badge">1</span><div class="feature-icon"></div><div class="feature-label">Registration</div></div>
        <div class="feature"><div class="feature-icon"></div><div class="feature-label">Insurance</div></div>
        <div class="feature"><span class="badge">1</span><div class="feature-icon"></div><div class="feature-label">CTP</div></div>
        <div class="feature"><div class="feature-icon"></div><div class="feature-label">Service</div></div>
        <div class="feature"><span class="badge">1</span><div class="feature-icon"></div><div class="feature-label">Finance</div></div>
        <div class="feature"><span class="badge">1</span><div class="feature-icon"></div><div class="feature-label">Roadside</div></div>
        <div class="feature"><div class="feature-icon"></div><div class="feature-label">Tolls &amp; Fines</div></div>
        <div class="feature"><div class="feature-icon"></div><div class="feature-label">Warranty</div></div>
      </div>
      <div class="pill pill-helper">Zentra Buddy</div>
      <div class="pill pill-new">What's New</div>
      <div class="toolbar">
        <svg viewBox="0 0 22 22"><path d="M5 9 V19 H17 V9 M11 14 V3 M7 7 L11 3 L15 7" fill="none" stroke="#4a8fd0" stroke-width="1.5"/></svg>
        <svg viewBox="0 0 22 22"><path d="M11 18 L4 11 A4 4 0 0 1 11 6 A4 4 0 0 1 18 11 Z" fill="none" stroke="#4a8fd0" stroke-width="1.5"/></svg>
        <svg viewBox="0 0 22 22"><path d="M5 6 H17 M9 6 V3 H13 V6 M6 6 L7 19 H15 L16 6 M9 9 V16 M13 9 V16" fill="none" stroke="#4a8fd0" stroke-width="1.5"/></svg>
      </div>
    </div>
  </div>

  <div class="callout callout-deal">Helps you find a better<br>finance or insurance deal.</div>
  <svg style="position:absolute;left:530px;top:628px" width="50" height="40" viewBox="0 0 50 40"><path d="M42 0 L50 22 L0 40 Z" fill="var(--blue)"/></svg>
  <svg style="position:absolute;left:452px;top:700px" width="36" height="46" viewBox="0 0 36 46"><path d="M18 0 L36 46 L0 46 Z" fill="var(--blue)"/></svg>
  <div class="callout callout-sell">Helps sell your car</div>

  <p class="pay-note">It will also pay a payment function<br>so you can pay,</p>
</div>
</body>
</html>
```